Bright Farm Stationery & Business Card
Stationery Designs for Agricultural Consulting company
Creative Brief
Bright & Fun-filled
Dennis & Marla Pickstone
427 Quillmoor Bend Lane Seffner, FL 33584
Dennis 813-555-0147
Marla 813-555-0183
brightfarmhelp@plowmail.example
Final design will need to have cards for 2 other salesmen info - name, cell & email would be different than above

```html
<!DOCTYPE html>
<html lang="en">
<head>
<meta charset="utf-8">
<title>Bright Farm Business Card</title>
<link rel="stylesheet" href="https://fonts.googleapis.com/css2?family=Arimo:wght@400;700&display=swap">
<style>
  :root {
    --page: #ffffff;
    --sky-light: #bfe4fb;
    --sky-mid: #6fbdf0;
    --sky-deep: #2f8fdc;
    --ink: #0d1b3a;
    --brand: #12357f;
    --sun: #f4b62a;
    --rule: #1d2f6b;
  }
  html, body {
    margin: 0;
    padding: 0;
    width: 1200px;
    height: 869px;
    overflow: hidden;
    background: var(--page);
    font-family: "Arimo", Arial, sans-serif;
  }
  .card {
    position: absolute;
    left: 32px;
    top: 104px;
    width: 1136px;
    height: 654px;
    overflow: hidden;
    background: linear-gradient(160deg, var(--sky-light) 0%, var(--sky-mid) 45%, var(--sky-deep) 100%);
    color: var(--ink);
  }
  .droplet-texture {
    position: absolute;
    left: 0;
    top: 0;
    width: 640px;
    height: 654px;
    background: radial-gradient(ellipse at 35% 55%, rgba(255,255,255,0.35) 0%, rgba(255,255,255,0) 70%);
  }
  .address {
    position: absolute;
    right: 28px;
    top: 20px;
    margin: 0;
    text-align: right;
    font-size: 23px;
    line-height: 34px;
    font-style: normal;
  }
  .brand {
    position: absolute;
    left: 100px;
    top: 160px;
    display: flex;
    align-items: center;
    gap: 28px;
  }
  .brand-name {
    margin: 0;
    font-size: 140px;
    font-weight: 700;
    line-height: 1;
    color: var(--brand);
    letter-spacing: -1px;
    white-space: nowrap;
  }
  .brand-dot {
    width: 78px;
    height: 78px;
    flex: none;
  }
  .contact {
    position: absolute;
    right: 28px;
    top: 370px;
    text-align: right;
  }
  .owners {
    margin: 0;
    font-size: 31px;
    line-height: 40px;
  }
  .email, .fax {
    margin: 0;
    font-size: 24px;
    line-height: 38px;
  }
  .phones {
    position: absolute;
    left: 640px;
    top: 510px;
    display: grid;
    grid-template-columns: 150px 3px 1fr;
    column-gap: 22px;
    font-size: 41px;
    line-height: 58px;
    width: 470px;
  }
  .phone-name { grid-column: 1; }
  .phone-rule {
    grid-column: 2;
    grid-row: 1 / span 2;
    background: var(--rule);
    width: 3px;
    margin: 6px 0;
  }
  .phone-number { grid-column: 3; white-space: nowrap; }
</style>
</head>
<body>
  <main class="card">
    <div class="droplet-texture" role="img" aria-label="Water droplets scattered across a blue background"></div>

    <address class="address">
      427 Quillmoor Bend Lane<br>
      Marrowdale, FL 30412
    </address>

    <div class="brand">
      <h1 class="brand-name">Bright Farm</h1>
      <svg class="brand-dot" viewBox="0 0 78 78" aria-hidden="true">
        <circle cx="39" cy="39" r="37" fill="var(--sun)"/>
      </svg>
    </div>

    <div class="contact">
      <p class="owners">Dennis &amp; Marla Pickstone</p>
      <p class="email">brightfarmhelp@plowmail.example</p>
      <p class="fax">Fax:813-555-0129</p>
    </div>

    <div class="phones">
      <span class="phone-name">Marla</span>
      <span class="phone-rule"></span>
      <span class="phone-number">813-555-0183</span>
      <span class="phone-name">Dennis</span>
      <span class="phone-number">813-555-0147</span>
    </div>
  </main>
</body>
</html>
```